New York City Sponsorship Page with Click Through Supporting Pages

Metro Workforce Guild, the leading New York City resource for HR Professionals is a membership organization with almost 2,000 individual members.

We need section/page(s) created for our current sponsorship offerings. Our platform is on ClubLedger Platform and we need capability to edit the page, etc. It must be HTML ready/coded.

Attached is the mock up of how we want the page to look (pages mockup pdf) as well as each of the categories which should be included (in the excel files). Our current page is here: http://www.metrowfguild.example/?page=sponsors and is not easy to read through. We want something that is visually appealing and clean but showcases all of the different ways to sponsor the Chapter.

Additionally, we are taking the information from this page and turning it into a brochure.

Target Market(s)

New York City Companies who have HR Professionals or services they want to attract or offer.

Coding

Coded - Design and coding required

Number of Pages Required

5+ page

Requirements
Must have
• Clean Look and feel, easy functionality, necessary information and purchases. Match the top navigation of current page. Opportunity for current sponsor logos to be highlighted on the page. Easy to update/maintain.
Nice to have
• Option to pay for sponsorships through the page using our credit card processor.
Should not have
• Overwhelming text in sections

```html
<!DOCTYPE html>
<html lang="en">
<head>
<meta charset="utf-8">
<title>Invitation for Sponsors – Metro Workforce Guild</title>
<link rel="stylesheet" href="https://fonts.googleapis.com/css2?family=Jost:wght@400;500;600;700&family=Open+Sans:wght@400;600;700&display=swap">
<style>
:root{
  --navy-top:#0e2a44;
  --nav-blue:#1a8fd0;
  --brand-red:#a51d10;
  --drop-red:#9b1b0f;
  --text-gray:#555;
  --text-dark:#1b1b1b;
  --strat-head:#0f5f96; --strat-body:#0b4873; --strat-price:#0a3d61;
  --prog-head:#00a6ea; --prog-body:#0891d4; --prog-price:#0782c2;
  --adv-head:#d9230b; --adv-body:#9c1a08; --adv-price:#891606;
  --cust-head:#3a3a3a; --cust-body:#1f1f1f; --cust-price:#171717;
  --panel-gray:#e8e8e8;
  --footer:#0d3b5c;
  --footer-bottom:#082a45;
  --white:#fff;
}
*{box-sizing:border-box;margin:0;padding:0}
html,body{width:1200px;height:2400px;overflow:hidden}
body{position:relative;background:var(--white);font-family:"Open Sans",Arial,sans-serif;color:var(--text-dark)}
.abs{position:absolute}

/* utility bar */
.utility-bar{left:0;top:0;width:1200px;height:40px;background:var(--navy-top)}
.utility-link{top:0;height:40px;display:flex;align-items:center;gap:6px;color:var(--white);font-family:"Jost",sans-serif;font-size:13px;white-space:nowrap}
.search-box{left:822px;top:6px;width:203px;height:28px;background:var(--white);display:flex;align-items:center;justify-content:space-between;padding:0 8px;font-size:12px;color:#999}
.social-top{left:1043px;top:10px;display:flex;gap:4px}
.social-top i{width:20px;height:20px;display:block;background:#3f8fd8}
.social-top i:last-child{background:#d1281f}

/* header */
.brand{left:24px;top:66px;display:flex;align-items:center;gap:10px}
.brand-dot{width:42px;height:42px;border-radius:50%;background:var(--navy-top)}
.brand-name{font-family:"Jost",sans-serif;font-weight:700;font-size:20px;color:var(--brand-red);line-height:1;white-space:nowrap}
.nav-item{top:89px;font-family:"Jost",sans-serif;font-weight:500;font-size:13.5px;line-height:20px;color:var(--nav-blue);text-transform:uppercase;white-space:nowrap}
.nav-item.active::before{content:"";position:absolute;left:-2px;right:-2px;top:-12px;height:2px;background:var(--brand-red)}
.dropdown{left:806px;top:120px;width:220px;background:var(--drop-red);font-family:"Jost",sans-serif;font-size:12px;color:var(--white);text-transform:uppercase;z-index:5;white-space:nowrap}
.dropdown li{list-style:none;height:32px;line-height:32px;padding-left:12px;border-bottom:1px solid #b0301f}
.dropdown li.current{background:#8a150a;border-top:3px solid var(--nav-blue);height:36px;line-height:33px}

/* hero */
.hero{left:0;top:149px;width:1200px;height:430px;background:linear-gradient(180deg,#05070d 0%,#0f1624 45%,#3a3540 80%,#5b4a3d 100%)}

/* intro */
.page-title{left:22px;top:630px;font-family:"Jost",sans-serif;font-weight:600;font-size:36px;letter-spacing:.3px;color:#111}
.title-rule{left:22px;top:680px;width:80px;height:5px;background:var(--nav-blue)}
.breadcrumb{left:22px;top:702px;font-size:14px;color:var(--brand-red)}
.share{left:22px;top:736px;font-size:13.5px;font-weight:600;color:#222}
.intro{left:24px;top:796px;width:740px;font-size:15px;line-height:1.3;color:var(--text-gray)}
.intro p{margin-bottom:6px}

/* tiers */
.tier{top:939px;width:269px;height:256px;color:var(--white);text-align:center}
.tier-head{height:69px;display:flex;align-items:center;justify-content:center;font-family:"Jost",sans-serif;font-weight:500;font-size:21px;line-height:1.1}
.tier-body{height:130px;display:flex;align-items:center;justify-content:center;padding:0 28px;font-size:13.5px;line-height:1.5}
.tier-price{height:57px;display:flex;align-items:center;justify-content:center;font-family:"Jost",sans-serif;font-weight:600;font-size:31px;border-top:1px solid rgba(255,255,255,.12)}
.tier-strategic{left:24px}.tier-strategic .tier-head{background:var(--strat-head)}.tier-strategic .tier-body{background:var(--strat-body)}.tier-strategic .tier-price{background:var(--strat-price)}
.tier-programs{left:320px}.tier-programs .tier-head{background:var(--prog-head)}.tier-programs .tier-body{background:var(--prog-body)}.tier-programs .tier-price{background:var(--prog-price)}
.tier-advertising{left:614px}.tier-advertising .tier-head{background:var(--adv-head)}.tier-advertising .tier-body{background:var(--adv-body)}.tier-advertising .tier-price{background:var(--adv-price)}
.tier-custom{left:907px}.tier-custom .tier-head{background:var(--cust-head)}.tier-custom .tier-body{background:var(--cust-body)}.tier-custom .tier-price{background:var(--cust-price)}

/* action links */
.action-links{left:24px;top:1286px;width:450px}
.action-links a{display:block;height:48px;line-height:46px;margin-bottom:8px;padding-left:11px;background:var(--panel-gray);border:1px solid #cfcfcf;font-family:"Jost",sans-serif;font-weight:500;font-size:17px;text-decoration:none}
.link-more{color:var(--nav-blue)}
.link-book{color:var(--brand-red)}
.link-contact{color:#222}

/* sponsors */
.sponsor-bar{left:24px;top:1533px;width:1155px;height:51px;background:#111;color:var(--white);font-family:"Jost",sans-serif;font-weight:500;font-size:17.5px;line-height:51px;padding-left:14px}
.sponsor-panel{left:24px;top:1584px;width:1155px;height:378px;background:var(--panel-gray);border:1px solid #d6d6d6;border-top:0}
.tier-label{font-family:"Jost",sans-serif;font-weight:500;font-size:26px;color:#111}
.sponsor-logo{background:var(--white);border:1px solid #b9b9b9;display:flex;align-items:center;justify-content:center;font-family:"Jost",sans-serif;font-weight:600;color:#1d3f7a;text-align:center;line-height:1.1}

/* footer */
.footer{left:0;top:2086px;width:1200px;height:271px;background:var(--footer);color:var(--white)}
.footer h3{font-family:"Jost",sans-serif;font-weight:500;font-size:21px;white-space:nowrap}
.footer-nav{left:24px;top:40px}
.footer-nav ul{margin-top:18px;padding-left:20px;font-size:14px;line-height:26px}
.footer-contact{left:294px;top:42px}
.footer-contact ul{list-style:none;margin-top:18px;font-size:14px;line-height:32px}
.footer-contact li{display:flex;align-items:center;gap:12px;white-space:nowrap}
.affiliate-badge{left:646px;top:40px;width:255px;height:179px;background:var(--white)}
.affiliate-badge i{position:absolute;left:0;right:0;top:38px;height:100px;background:#3a63a8}
.footer-connect{left:987px;top:38px}
.social-circles{display:flex;gap:5px;margin-top:28px;margin-left:8px}
.social-circles i{width:26px;height:26px;border-radius:50%;background:#9aa8b5;display:block}
.footer-bottom{left:0;top:2357px;width:1200px;height:43px;background:var(--footer-bottom);color:var(--white);font-size:12.5px;text-align:center;line-height:43px}
</style>
</head>
<body>

<div class="utility-bar abs"></div>
<span class="utility-link abs" style="left:469px"><svg width="13" height="13" viewBox="0 0 24 24"><path fill="#fff" d="M6.6 10.8c1.4 2.8 3.8 5.1 6.6 6.6l2.2-2.2c.3-.3.7-.4 1-.2 1.1.4 2.3.6 3.6.6.6 0 1 .4 1 1V20c0 .6-.4 1-1 1C10.6 21 3 13.4 3 4c0-.6.4-1 1-1h3.5c.6 0 1 .4 1 1 0 1.3.2 2.5.6 3.6.1.3 0 .7-.2 1z"/></svg>CONTACT US</span>
<span class="utility-link abs" style="left:592px"><svg width="12" height="12" viewBox="0 0 24 24"><circle cx="12" cy="7" r="5" fill="#fff"/><path fill="#fff" d="M2 23c0-6 4.5-9 10-9s10 3 10 9z"/></svg>SIGN IN</span>
<span class="utility-link abs" style="left:689px"><svg width="22" height="13" viewBox="0 0 30 18"><path fill="#fff" d="M1 7l7-5 6 3 6-3 9 5-4 3-8 6c-1 1-2 1-3 0L6 11z"/></svg>JOIN/RENEW</span>
<div class="search-box abs">Search
  <svg width="20" height="20" viewBox="0 0 24 24"><circle cx="10" cy="10" r="7" fill="none" stroke="#111" stroke-width="2.6"/><path d="M15 15l7 7" stroke="#111" stroke-width="3"/></svg>
</div>
<div class="social-top abs"><i></i><i></i><i></i><i></i><i></i></div>

<div class="brand abs"><span class="brand-dot"></span><span class="brand-name">Metro Workforce Guild</span></div>
<nav>
  <span class="nav-item abs" style="left:379px">Our New Website</span>
  <span class="nav-item abs" style="left:530px">About Us</span>
  <span class="nav-item abs" style="left:621px">Membership</span>
  <span class="nav-item abs" style="left:734px">Events</span>
  <span class="nav-item active abs" style="left:806px">Sponsorships</span>
  <span class="nav-item abs" style="left:936px">Career Center</span>
  <span class="nav-item abs" style="left:1072px">HR Resources</span>
</nav>

<div class="hero abs" role="img" aria-label="Photograph of the New York City skyline lit up at night"></div>

<ul class="dropdown abs">
  <li class="current">Sponsorship Opportunities</li>
  <li>Strategic Partnership</li>
  <li>Programs / Events</li>
  <li>Advertising / Promotion</li>
</ul>

<h1 class="page-title abs">INVITATION FOR SPONSORS</h1>
<div class="title-rule abs"></div>
<div class="breadcrumb abs">Sponsorships » Sponsorship Opportunities</div>
<div class="share abs">Share |</div>
<div class="intro abs">
  <p>Thank you for your interest in Metro Workforce Guild.</p>
  <p>As a premier National HR Society chapter, we offer many opportunities to increase your exposure to the New York City HR community.</p>
  <p style="color:#444">Choose the sponsorship category that best meets your needs:</p>
</div>

<div class="tier tier-strategic abs">
  <div class="tier-head">Strategic<br>Partnership</div>
  <div class="tier-body">Opportunities for a strategic sponsorship at different levels, each providing a valuable set of great benefits</div>
  <div class="tier-price">$3,500+</div>
</div>
<div class="tier tier-programs abs">
  <div class="tier-head">Programs /<br>Events</div>
  <div class="tier-body">Opportunities for a strategic sponsorship at different levels, each providing a valuable set of great benefits</div>
  <div class="tier-price">$500+</div>
</div>
<div class="tier tier-advertising abs">
  <div class="tier-head">Advertising /<br>Promotion</div>
  <div class="tier-body">Opportunities for a strategic sponsorship at different levels, each providing a valuable set of great benefits</div>
  <div class="tier-price">$150+</div>
</div>
<div class="tier tier-custom abs">
  <div class="tier-head">Custom</div>
  <div class="tier-body">Build your own sponsorship program from our variety of opportunities</div>
  <div class="tier-price">$250+</div>
</div>

<div class="action-links abs">
  <a class="link-more" href="#">More about our sponsorship packages</a>
  <a class="link-book" href="#">Book your sponsorship package</a>
  <a class="link-contact" href="#">Contact our sponsorship team</a>
</div>

<div class="sponsor-bar abs">Thank You to Our Corporate Sponsors</div>
<div class="sponsor-panel abs"></div>
<div class="tier-label abs" style="left:40px;top:1618px">Gold</div>
<div class="sponsor-logo abs" style="left:40px;top:1664px;width:299px;height:66px;font-size:30px">Harlow &amp; Brandt</div>
<div class="sponsor-logo abs" style="left:365px;top:1653px;width:239px;height:86px;font-size:21px">TransitPerks<br>Solutions</div>
<div class="tier-label abs" style="left:36px;top:1788px">Silver</div>
<div class="sponsor-logo abs" style="left:40px;top:1834px;width:323px;height:75px;font-size:36px">Staffwell</div>
<div class="sponsor-logo abs" style="left:389px;top:1834px;width:323px;height:75px;font-size:22px;color:#222">Bastion Benefits<br>&amp; Financial Group</div>

<footer class="footer abs">
  <div class="footer-nav abs">
    <h3>Navigation</h3>
    <ul><li>About Us</li><li>Membership</li><li>Events</li><li>Career Center</li><li>Sponsorships</li><li>HR Resources</li></ul>
  </div>
  <div class="footer-contact abs">
    <h3>Contact us</h3>
    <ul>
      <li><svg width="16" height="16" viewBox="0 0 24 24"><path fill="#fff" d="M6.6 10.8c1.4 2.8 3.8 5.1 6.6 6.6l2.2-2.2c.3-.3.7-.4 1-.2 1.1.4 2.3.6 3.6.6.6 0 1 .4 1 1V20c0 .6-.4 1-1 1C10.6 21 3 13.4 3 4c0-.6.4-1 1-1h3.5c.6 0 1 .4 1 1 0 1.3.2 2.5.6 3.6.1.3 0 .7-.2 1z"/></svg>Phone: 877-555-0142</li>
      <li><svg width="18" height="16" viewBox="0 0 24 22"><rect x="6" y="1" width="12" height="6" fill="none" stroke="#fff" stroke-width="2"/><rect x="1" y="7" width="22" height="9" rx="1" fill="#fff"/><rect x="6" y="13" width="12" height="8" fill="var(--footer)" stroke="#fff" stroke-width="2"/></svg>Fax: 609-555-0187</li>
      <li><svg width="18" height="14" viewBox="0 0 24 18"><rect x="1" y="1" width="22" height="16" fill="none" stroke="#fff" stroke-width="2"/><path d="M1 1l11 9 11-9" fill="none" stroke="#fff" stroke-width="2"/></svg>Email: info@metrowfguild.example</li>
    </ul>
  </div>
  <div class="affiliate-badge abs"><i></i></div>
  <div class="footer-connect abs">
    <h3>Connect With Us</h3>
    <div class="social-circles"><i></i><i></i><i></i><i></i><i></i></div>
  </div>
</footer>
<div class="footer-bottom abs">©2016 Metro Workforce Guild ALL RIGHT RESERVED</div>

</body>
</html>
```